Business Card Design Project - bel soravin group

dear Sirs

we need business card design for our group ( BEL Soravin Group ) , i have got the Logo design of our group from pixel harbor in previous , so all need details relating to our group i think available with you, as well as the the chosen logo design

we hope to provide us with business card logo that to be appropaite and satisfactory to us .

thanks

note : logo design of our group is attached .
Updates

Reason: please extend the deadline of my project for additional 15 days because i didn't received appropriate design for our gruop yet . kindly beaware that i have received 77 design till now , supossed to send me 200-250 design at least . thanks

Target Market(s)

contents
-

name : Korvan EL Mistrani

position : Operation Manager

Industry/Entity Type

Business

Requirements
Must have

• person name

group logo
Nice to have
• logo color matching with back background

```html
<!DOCTYPE html>
<html lang="en">
<head>
<meta charset="utf-8">
<title>BEL Soravin Group – Business Card</title>
<link href="https://fonts.googleapis.com/css2?family=Jost:wght@400;500&family=Crimson+Text:wght@400;600&display=swap" rel="stylesheet">
<style>
  :root {
    --backdrop: #8f8f8f;
    --card-white: #f7f7f5;
    --brand-blue: #1d6fa5;
    --gold: #c9a23e;
    --gold-light: #d7b24f;
    --gold-dark: #b48c2f;
    --band-pale: #efdca6;
    --ink-grey: #6d6d6d;
    --ink-white: #fbf6e6;
  }
  * { box-sizing: border-box; margin: 0; padding: 0; }
  html, body { width: 1200px; height: 788px; overflow: hidden; }
  body {
    background: var(--backdrop);
    font-family: "Jost", sans-serif;
    display: flex;
    align-items: center;
    justify-content: center;
    gap: 50px;
  }
  .card {
    position: relative;
    width: 540px;
    height: 310px;
    border-radius: 3px;
    box-shadow: 0 8px 22px rgba(0,0,0,.28);
    overflow: hidden;
  }

  /* Front side */
  .card--front { background: var(--card-white); }
  .holder {
    position: absolute; top: 26px; left: 0;
    padding-left: 30px;
    border-left: 14px solid var(--gold);
  }
  .holder__name {
    font-family: "Crimson Text", serif;
    font-weight: 600;
    font-size: 22px;
    color: var(--brand-blue);
    line-height: 1.1;
  }
  .holder__role {
    font-family: "Crimson Text", serif;
    font-size: 15px;
    color: var(--ink-grey);
  }
  .brand {
    position: absolute; left: 0; right: 0; top: 112px;
    display: flex; align-items: center; justify-content: center; gap: 14px;
  }
  .brand__square { width: 22px; height: 22px; background: var(--gold); }
  .brand__name {
    font-family: "Jost", sans-serif;
    font-weight: 500;
    font-size: 40px;
    letter-spacing: 1px;
    color: var(--brand-blue);
  }
  .contact-band {
    position: absolute; left: 0; right: 0; bottom: 0;
    height: 86px;
    background: linear-gradient(var(--card-white) 0 14px, var(--band-pale) 14px);
    border-bottom: 10px solid var(--band-pale);
    padding: 22px 36px 0;
    display: flex; justify-content: space-between; align-items: center;
  }
  .contact {
    display: flex; align-items: center; gap: 8px;
    font-size: 16px; color: var(--ink-grey);
  }
  .contact svg { width: 15px; height: 15px; fill: var(--gold); }

  /* Back side */
  .card--back {
    background: linear-gradient(160deg, var(--gold-light), var(--gold) 55%, var(--gold-dark));
    color: var(--ink-white);
  }
  .back-brand {
    position: absolute; top: 46px; left: 0; right: 0;
    display: flex; justify-content: center; align-items: center; gap: 10px;
  }
  .back-brand__square { width: 16px; height: 16px; background: var(--ink-white); }
  .back-brand__name { font-weight: 500; font-size: 26px; letter-spacing: 1px; }
  .address {
    position: absolute; top: 118px; left: 36px; width: 220px;
    font-size: 14px; line-height: 1.6;
    display: flex; gap: 8px;
  }
  .phones {
    position: absolute; top: 160px; right: 36px;
    font-size: 14px; line-height: 1.6;
  }
  .phones li { list-style: none; display: flex; align-items: center; gap: 8px; }
  .card--back svg { width: 13px; height: 13px; fill: var(--ink-white); flex: none; margin-top: 4px; }
  .phones svg { margin-top: 0; }
  .website {
    position: absolute; bottom: 34px; left: 0; right: 0;
    text-align: center; font-size: 20px; letter-spacing: 1px;
  }
</style>
</head>
<body>

  <section class="card card--front">
    <div class="holder">
      <p class="holder__name">Korvan EL Mistrani</p>
      <p class="holder__role">Operation Manager</p>
    </div>
    <div class="brand">
      <span class="brand__square"></span>
      <span class="brand__name">BEL SORAVIN</span>
    </div>
    <div class="contact-band">
      <p class="contact">
        <svg viewBox="0 0 16 16"><path d="M4 0h8a1 1 0 0 1 1 1v14a1 1 0 0 1-1 1H4a1 1 0 0 1-1-1V1a1 1 0 0 1 1-1zm1 2v10h6V2zm3 11a1 1 0 1 0 0 2 1 1 0 0 0 0-2z"/></svg>
        (014) 20 555 38 71
      </p>
      <p class="contact">
        <svg viewBox="0 0 16 16"><path d="M0 3h16v10H0zm1 1.2V12h14V4.2L8 9z"/><path d="M1 3h14L8 8z"/></svg>
        korvan@bel-soravin.com
      </p>
    </div>
  </section>

  <section class="card card--back">
    <div class="back-brand">
      <span class="back-brand__square"></span>
      <span class="back-brand__name">BEL SORAVIN GROUP</span>
    </div>
    <p class="address">
      <svg viewBox="0 0 16 16"><path d="M8 1 0 8h2v7h4v-4h4v4h4V8h2z"/></svg>
      <span>Lorem Ipsum is simply dummy text of the printing</span>
    </p>
    <ul class="phones">
      <li><svg viewBox="0 0 16 16"><path d="M3.6 1 6 4.4 4.6 6.2a10 10 0 0 0 5.2 5.2L11.6 10 15 12.4 13.6 15C6.6 15 1 9.4 1 2.4z"/></svg>(014) 20 555 38 71</li>
      <li><svg viewBox="0 0 16 16"><path d="M4 1h6l2 2v3H4zM1 7h14v7H1zm3 2v1h2V9zm4 0v1h2V9z"/></svg>(014) 20 555 38 72</li>
    </ul>
    <p class="website">www.bel-soravin.com</p>
  </section>

</body>
</html>
```